Regenerative Medicine Brochure

I want a clean modern bi-fold or tri-fold brochure. We offer non-surgical joint repair for knees, shoulders, and hips. We have many services available including regenerative medicine including stem cell allograft, palatelet rich plasma, prolotherapy, triggerpoint injection, chiropractic and rehab therapies. We are a modern multidisciplinary clinic in coastal California. My logo is already complete and is a vibrant green color. I prefer lots of white space with some areas for service description and what conditions may benefit from the services. Design should convey modern treatments, upscale office and practice, and our target audience is older adults who want to maintain an active pain-free lifestyle.

Target Market(s)

Sports injuries, athletes, seniors who are active, knee pain, shoulder pain, arthritis.

Industry/Entity Type

Alternative Medicine

Font styles to use
Serif

Colors
9bcb3c

Requirements
Must have
• Small white space where we can write date, time, location of next event/class. Colors in brochure to coordinate with logo colors provided.

```html
<!DOCTYPE html>
<html lang="en">
<head>
<meta charset="utf-8">
<title>Renewal Motion Clinic – Brochure Cover</title>
<link href="https://fonts.googleapis.com/css2?family=Arimo:wght@400;500;700&display=swap" rel="stylesheet">
<style>
  :root {
    --brand-green: #9bcb3c;
    --ink: #2e2c38;
    --ink-body: #333238;
    --ink-soft: #5b5f6b;
    --paper: #f4f5f7;
    --white: #ffffff;
  }
  * { margin: 0; padding: 0; box-sizing: border-box; }
  html, body { width: 1200px; height: 927px; overflow: hidden; }
  body {
    font-family: "Arimo", Arial, sans-serif;
    background: var(--paper);
    color: var(--ink);
  }
  .brochure {
    position: relative;
    width: 1200px;
    height: 927px;
    overflow: hidden;
    background: linear-gradient(180deg, #eceef1 0%, #f7f8f9 45%, #f3f4f6 100%);
  }
  .corner-pattern {
    position: absolute;
    left: 0; top: 0;
    width: 385px; height: 480px;
    background: radial-gradient(ellipse at 0% 40%, rgba(74,74,82,0.55) 0%, rgba(74,74,82,0.25) 40%, rgba(74,74,82,0) 75%);
  }
  .dot-swirl {
    position: absolute;
    left: 502px; top: 309px;
    width: 290px; height: 183px;
    background: radial-gradient(ellipse at 55% 50%, rgba(160,166,172,0.35) 0%, rgba(160,166,172,0) 70%);
  }
  .athlete-photo {
    position: absolute;
    left: 806px; top: 0;
    width: 347px; height: 786px;
    background: linear-gradient(180deg, #d8c2b2 0%, #cfb3a2 35%, #9a9ca3 48%, #d4b8a6 65%, #c9ac9b 85%, #3a3e4c 100%);
    opacity: 0.85;
    border-radius: 40% 40% 10% 10% / 12% 12% 4% 4%;
  }
  .headline {
    position: absolute;
    left: 419px; top: 310px;
    font-size: 67px;
    font-weight: 400;
    letter-spacing: -1px;
    color: var(--ink);
    line-height: 1;
  }
  .subhead {
    position: absolute;
    left: 567px; top: 379px;
    font-size: 22px;
    color: var(--ink-soft);
    letter-spacing: 0.2px;
    line-height: 1;
  }
  .contact {
    position: absolute;
    left: 0; top: 474px;
    width: 398px;
    text-align: center;
  }
  .contact-title { font-size: 20.5px; font-weight: 500; color: var(--ink); line-height: 1.25; }
  .contact-phone { font-size: 20.5px; color: var(--ink-soft); margin-top: 5px; line-height: 1.25; }
  .intro {
    position: absolute;
    left: 41px; top: 556px;
    width: 314px;
    font-size: 13.6px;
    font-weight: 500;
    line-height: 21.1px;
    color: var(--ink-body);
  }
  .intro-line {
    display: block;
    text-align: justify;
    text-align-last: justify;
    white-space: nowrap;
  }
  .footer-band {
    position: absolute;
    left: 0; top: 786px;
    width: 1200px; height: 141px;
    background: var(--brand-green);
  }
  .event-details {
    position: absolute;
    left: 0; top: 39px;
    width: 394px;
    text-align: center;
    color: var(--white);
  }
  .event-date { font-size: 13.5px; line-height: 18px; }
  .event-address { font-size: 14px; line-height: 18px; margin-top: 4px; }
  .event-email { font-size: 12px; letter-spacing: 1.2px; line-height: 18px; margin-top: 4px; }
  .brand-badge {
    position: absolute;
    left: 489px; top: 731px;
    width: 221px; height: 101px;
    background: var(--brand-green);
    display: flex; align-items: center; justify-content: center;
  }
  .brand-badge-frame {
    width: 201px; height: 81px;
    border: 2px solid var(--white);
    display: flex; align-items: center; justify-content: center;
    font-size: 48px; font-weight: 700; color: var(--white);
    letter-spacing: -1px;
  }
  .brand-name {
    position: absolute;
    right: 40px; top: 52px;
    font-size: 26px;
    font-weight: 400;
    color: var(--white);
    letter-spacing: 0.5px;
  }
</style>
</head>
<body>
  <main class="brochure">
    <div class="corner-pattern" role="img" aria-label="Decorative field of small dark triangles fading toward the centre"></div>
    <div class="athlete-photo" role="img" aria-label="Photograph of an athletic woman in sportswear jumping with one knee raised, knees highlighted in red"></div>
    <div class="dot-swirl" role="img" aria-label="Decorative swirl of grey dots"></div>

    <h1 class="headline">IT WILL</h1>
    <p class="subhead">START AGAIN</p>

    <section class="contact">
      <p class="contact-title">Contact Us To Sign Up Today</p>
      <p class="contact-phone">555.204.1836</p>
    </section>

    <p class="intro">
      <span class="intro-line">For joint arthritis and muscle pain and injuries, the</span>
      <span class="intro-line">team at Renewal Motion Clinic offers minimally</span>
      <span class="intro-line">invasive regenerative medicine techniques to</span>
      <span class="intro-line">help you recover from chronic pain. Located in</span>
      <span class="intro-line">Seaside Cove, California, the medical team utilizes</span>
      <span class="intro-line">advanced restorative techniques to support the</span>
      <span class="intro-line">natural healing of injured joints and soft tissues</span>
      <span class="intro-line">without the need for surgery. To learn more,</span>
      <span class="intro-line">schedule a consultation online or by phone today.</span>
    </p>

    <footer class="footer-band">
      <div class="event-details">
        <p class="event-date">March 22.29th</p>
        <p class="event-address">420 harbor lane, seaside cove, ca90000</p>
        <p class="event-email">hello@RenewalMotionClinic.com</p>
      </div>
      <p class="brand-name">Renewal Motion Clinic</p>
    </footer>

    <div class="brand-badge">
      <div class="brand-badge-frame">RMC</div>
    </div>
  </main>
</body>
</html>
```